Website Design for Arena on Draft: Sports TV for bars and restaurants

We need a website design for a streaming service called Arena on Draft. Arena on Draft provides sports programming to bars and restaurants across the United States and Canada. We would like to see a design that uses the colors of red, black, gold, and white. The final design should be functional business site, designed primarily for registration and ordering capabilities. In addition to a Registration and an Order page, we would like to see the following pages: Upcoming Events, FAQs, and About. We would also like to see an option at the top of the page to switch between languages (English and Spanish)

Target Market(s)

Male, 21-45 years old

Industry/Entity Type

Sports Bar

Number of Pages Required

5+ page

Font styles to use
Serif
Sans Serif

Requirements
Must have
• The project must have an easy to use registration page that include the following fields: Establishment's Name, Manager's name and contact info (phone number and email), and a field to upload a picture of their fire code. The project also must have an easy to use Upcoming events page with the ability to upload a fight's promotional poster.
Nice to have
• Nice to have an area on the main home page for testimonials and a scrolling ticker to put our partner's logos.

```html
<!DOCTYPE html>
<html lang="en">
<head>
<meta charset="utf-8">
<title>Arena on Draft — Sports TV for Bars and Restaurants</title>
<link href="https://fonts.googleapis.com/css2?family=Exo+2:wght@400;500;600;700&display=swap" rel="stylesheet">
<style>
:root{
  --red:#a80000;
  --red-deep:#9c0c0c;
  --gold:#f2b705;
  --black:#0a0a0a;
  --ink:#222222;
  --muted:#8a8a8a;
  --white:#ffffff;
  --paper:#ffffff;
  --footer-bar:#2a0c0c;
}
*{box-sizing:border-box;margin:0;padding:0}
html,body{width:1200px;height:3448px;overflow:hidden}
body{font-family:"Exo 2",sans-serif;color:var(--ink);background:var(--paper);position:relative}
.section{position:absolute;left:0;width:1200px}
.abs{position:absolute}
.btn{position:absolute;background:var(--red);color:var(--white);font-weight:600;font-size:15px;text-transform:uppercase;display:flex;align-items:center;justify-content:center;letter-spacing:.3px}
.section-title{position:absolute;left:0;width:1200px;text-align:center;font-weight:700;font-size:34px;letter-spacing:1px;text-transform:uppercase}

/* hero */
.hero{top:0;height:575px}
.hero-photo{position:absolute;inset:0;background:radial-gradient(ellipse at 25% 45%,#5a3a2a 0%,#2b1a12 35%,#120a07 70%),linear-gradient(90deg,#1a0f0a,#2a1608 60%,#120906)}
.hero-shade{position:absolute;inset:0;background:linear-gradient(90deg,rgba(0,0,0,.15),rgba(0,0,0,.55))}
.brand{position:absolute;left:46px;top:44px;display:flex;align-items:center;gap:10px;color:var(--white);font-weight:700;font-size:20px}
.brand-dot{width:16px;height:16px;border-radius:50%;background:var(--red)}
.account{position:absolute;top:38px;right:82px;display:flex;gap:10px}
.account a{background:var(--red);color:var(--white);font-size:12px;text-decoration:none;padding:7px 16px;font-weight:500}
.main-nav{position:absolute;top:121px;left:0;width:1200px;display:flex;justify-content:center;gap:48px;font-size:13px;font-weight:600;text-transform:uppercase;color:var(--white)}
.main-nav .active{color:var(--gold)}
.hero-copy{position:absolute;left:690px;top:278px;width:440px;text-align:center}
.hero-welcome{color:var(--white);font-size:23px;font-weight:500}
.hero-name{color:var(--gold);font-size:50px;font-weight:700;letter-spacing:1px;margin-top:2px;text-transform:uppercase}

/* about */
.about{top:575px;height:345px}
.about-photo{position:absolute;inset:0;background:linear-gradient(180deg,#1b110c,#0d0806 60%,#150c08)}
.about .section-title{top:622px;color:var(--white)}
.about-text{position:absolute;left:195px;top:688px;width:810px;text-align:center;color:#e8e8e8;font-size:13.5px;line-height:22px}

/* events */
.events{top:920px;height:540px;background:var(--paper)}
.event-card{position:absolute;top:1062px;width:294px;text-align:center}
.event-card.featured::before{content:"";position:absolute;left:-16px;top:-14px;width:326px;height:345px;border:1px solid #e2e2e2;box-shadow:0 2px 8px rgba(0,0,0,.08)}
.event-photo{position:relative;height:140px}
.event-name{position:relative;margin-top:28px;font-weight:700;font-size:15px;letter-spacing:1px;color:var(--ink)}
.event-text{position:relative;margin:8px auto 0;width:260px;font-size:13px;line-height:18px;color:#b0b0b0}
.event-card .btn{left:73px;top:281px;width:148px;height:37px}

/* upcoming */
.upcoming{top:1460px;height:517px;background:var(--black)}
.match{position:absolute;top:1582px;width:502px;height:269px}
.match-photo{position:absolute;inset:0}
.match-date{position:absolute;left:0;bottom:0;width:104px;height:113px;background:var(--gold);display:flex;flex-direction:column;align-items:center;justify-content:center;gap:14px;font-weight:700;font-size:19px;color:var(--ink)}
.match-info{position:absolute;left:104px;right:0;bottom:0;height:113px;background:rgba(255,255,255,.8);padding:20px 14px;font-size:13px;line-height:16px;color:var(--ink)}
.match-info strong{display:block;font-weight:700}
.match-info em{font-style:normal;font-weight:700;text-transform:uppercase}

/* testimonial */
.testimonial{top:1977px;height:391px;background:var(--paper)}
.quote-mark{position:absolute;color:var(--red);font-size:48px;font-weight:700;line-height:1}
.quote-text{position:absolute;left:270px;top:2102px;width:660px;text-align:center;font-style:italic;font-size:13px;line-height:20px;color:var(--muted)}
.avatar{position:absolute;left:562px;top:2158px;width:76px;height:76px;border-radius:50%;border:3px solid #f0f0f0}
.client-name{position:absolute;left:0;top:2254px;width:1200px;text-align:center;color:var(--red);font-size:12px;font-weight:600;text-transform:uppercase}
.dots{position:absolute;left:0;top:2294px;width:1200px;display:flex;justify-content:center;gap:8px}
.dots span{width:10px;height:10px;border-radius:50%;background:#e5b0b0}
.dots span.on{background:var(--red)}

/* partners */
.partners{top:2368px;height:310px}
.partners-photo{position:absolute;inset:0;background:linear-gradient(90deg,#1a0d08,#2c1710 40%,#1c0f0a 70%,#0e0806)}
.partners .section-title{top:2418px;color:var(--white)}
.partner{position:absolute;top:2506px;width:152px;height:110px;background:var(--white);display:flex;align-items:center;justify-content:center}

/* contact */
.contact{top:2678px;height:494px;background:var(--paper)}
.field{position:absolute;background:var(--white);box-shadow:0 2px 8px rgba(0,0,0,.12);font-size:12px;color:#555;padding:13px 20px;text-transform:uppercase}

/* footer */
.site-footer{top:3172px;height:235px;background:var(--red-deep);color:var(--white)}
.footer-head{position:absolute;font-weight:700;font-size:15px;text-transform:uppercase;letter-spacing:.5px}
.footer-links{position:absolute;left:175px;top:3232px;list-style:none;font-size:12px;font-weight:700;line-height:31px}
.footer-brand{position:absolute;left:520px;top:3212px;width:160px;text-align:center;font-weight:700;font-size:22px;line-height:26px}
.socials{position:absolute;left:513px;top:3329px;display:flex;gap:20px}
.socials span{width:28px;height:28px;border-radius:50%;border:2px solid rgba(255,255,255,.55)}
.address{position:absolute;left:878px;top:3232px;width:220px;font-size:11.5px;line-height:17px}
.address b{display:block;font-size:11px;text-transform:uppercase;margin-top:10px}
.address b:first-child{margin-top:0}
.copyright{position:absolute;left:0;top:3407px;width:1200px;height:41px;background:var(--footer-bar);color:#e6e6e6;font-size:12px;display:flex;align-items:center;justify-content:center}
</style>
</head>
<body>

<header class="section hero">
  <div class="hero-photo" role="img" aria-label="Fans cheering while watching a game in a dimly lit sports bar"></div>
  <div class="hero-shade"></div>
  <div class="brand"><span class="brand-dot"></span>Arena on Draft</div>
  <div class="account"><a href="#">Log-In</a><a href="#">Register</a></div>
  <nav class="main-nav">
    <span class="active">Home</span><span>About</span><span>Upcoming Events ˅</span><span>FAQs</span><span>Contact Us</span>
  </nav>
  <div class="hero-copy">
    <div class="hero-welcome">WELCOME TO OUR</div>
    <div class="hero-name">Arena on Draft</div>
  </div>
  <a class="btn" style="left:832px;top:391px;width:150px;height:48px">Book Now</a>
</header>

<section class="section about">
  <div class="about-photo" role="img" aria-label="Dark sports bar interior with warm lights"></div>
</section>
<h2 class="section-title" style="top:622px;color:var(--white)">About Us</h2>
<p class="about-text">Lorem Ipsum is simply dummy text of the printing and typesetting industry. Lorem Ipsum has been the industry's standard dummy text ever since the 1500s, when an unknown printer took a galley of type and scrambled it to make a type specimen book. It has survived not only five centuries, but also the leap into electronic typesetting, remaining essentially unchanged. It was popularised in the 1960s with the release of</p>
<a class="btn" style="left:524px;top:806px;width:152px;height:40px">Read More</a>

<section class="section events"></section>
<h2 class="section-title" style="top:972px;color:var(--ink)">Our Events</h2>

<article class="event-card" style="left:101px">
  <div class="event-photo" role="img" aria-label="Hockey players battling for the puck on ice" style="background:linear-gradient(180deg,#c9cdd2,#eef0f2 55%,#d8dbde)"></div>
  <div class="event-name">HOCKEY</div>
  <p class="event-text">Lorem Ipsum is simply dummy text of the printing and typesetting industry. Lorem Ipsum has been the industry's standard dummy text ever since 1500s.</p>
  <a class="btn">Book Now</a>
</article>
<article class="event-card featured" style="left:453px">
  <div class="event-photo" role="img" aria-label="Football players challenging for the ball on a green pitch" style="background:linear-gradient(180deg,#2c3a44,#3d6b3a 55%,#4c8a3c)"></div>
  <div class="event-name">FOOTBALL</div>
  <p class="event-text">Lorem Ipsum is simply dummy text of the printing and typesetting industry. Lorem Ipsum has been the industry's standard dummy text ever since 1500s.</p>
  <a class="btn">Book Now</a>
</article>
<article class="event-card" style="left:805px">
  <div class="event-photo" role="img" aria-label="Basketball dropping through the hoop net" style="background:radial-gradient(ellipse at 60% 70%,#b5622a,#4a2a1c 55%,#1d1210)"></div>
  <div class="event-name">BASKETBALL</div>
  <p class="event-text">Lorem Ipsum is simply dummy text of the printing and typesetting industry. Lorem Ipsum has been the industry's standard dummy text ever since 1500s.</p>
  <a class="btn">Book Now</a>
</article>

<section class="section upcoming"></section>
<h2 class="section-title" style="top:1511px;color:var(--white)">Upcoming Events</h2>

<article class="match" style="left:85px">
  <div class="match-photo" role="img" aria-label="Friends toasting drinks together at a bar" style="background:linear-gradient(135deg,#6b3a1c,#c7873f 50%,#5a2c14)"></div>
  <div class="match-date">
    <svg width="26" height="26" viewBox="0 0 26 26" aria-hidden="true"><rect x="2" y="4" width="22" height="20" fill="none" stroke="#222" stroke-width="2.4"/><rect x="2" y="4" width="22" height="5" fill="#222"/><rect x="7" y="1" width="2.5" height="6" fill="#222"/><rect x="16.5" y="1" width="2.5" height="6" fill="#222"/><g fill="#222"><rect x="6" y="12" width="3" height="3"/><rect x="11.5" y="12" width="3" height="3"/><rect x="17" y="12" width="3" height="3"/><rect x="6" y="17.5" width="3" height="3"/><rect x="11.5" y="17.5" width="3" height="3"/><rect x="17" y="17.5" width="3" height="3"/></g></svg>
    JULY 30
  </div>
  <div class="match-info"><strong>Lorem Ipsum is simply dummy text of the printing and typesetting industry.</strong>Lorem Ipsum is simply dummy text of the printing and typesetting industry. <em>Read More</em></div>
</article>
<article class="match" style="left:613px">
  <div class="match-photo" role="img" aria-label="Fans in red jerseys watching a match at a bar counter" style="background:linear-gradient(135deg,#3a2418,#8a5a34 50%,#4a2c1a)"></div>
  <div class="match-date">
    <svg width="26" height="26" viewBox="0 0 26 26" aria-hidden="true"><rect x="2" y="4" width="22" height="20" fill="none" stroke="#222" stroke-width="2.4"/><rect x="2" y="4" width="22" height="5" fill="#222"/><rect x="7" y="1" width="2.5" height="6" fill="#222"/><rect x="16.5" y="1" width="2.5" height="6" fill="#222"/><g fill="#222"><rect x="6" y="12" width="3" height="3"/><rect x="11.5" y="12" width="3" height="3"/><rect x="17" y="12" width="3" height="3"/><rect x="6" y="17.5" width="3" height="3"/><rect x="11.5" y="17.5" width="3" height="3"/><rect x="17" y="17.5" width="3" height="3"/></g></svg>
    JULY 30
  </div>
  <div class="match-info"><strong>Lorem Ipsum is simply dummy text of the printing and typesetting industry.</strong>Lorem Ipsum is simply dummy text of the printing and typesetting industry. <em>Read More</em></div>
</article>
<a class="btn" style="left:525px;top:1879px;width:150px;height:40px">View All</a>

<section class="section testimonial"></section>
<h2 class="section-title" style="top:2031px;color:var(--ink)">Testimonial</h2>
<span class="quote-mark" style="left:236px;top:2092px">“</span>
<p class="quote-text">Contrary to popular belief, Lorem Ipsum is not simply random text. It has roots in a piece of classical Latin literature from 45 BC, making it over 2000 years old</p>
<span class="quote-mark" style="left:938px;top:2124px">”</span>
<div class="avatar" role="img" aria-label="Portrait of the client giving the testimonial" style="background:linear-gradient(180deg,#7a3a2a,#d9a890)"></div>
<div class="client-name">Mara Lenz</div>
<div class="dots"><span></span><span class="on"></span><span></span></div>

<section class="section partners">
  <div class="partners-photo" role="img" aria-label="Blurred sports bar interior"></div>
</section>
<h2 class="section-title" style="top:2418px;color:var(--white)">Our Partner's Logos</h2>
<div class="partner" style="left:85px"><svg width="90" height="90" aria-hidden="true"><circle cx="45" cy="45" r="36" fill="none" stroke="#222" stroke-width="3"/></svg></div>
<div class="partner" style="left:262px"><svg width="90" height="90" aria-hidden="true"><circle cx="45" cy="45" r="36" fill="#222"/></svg></div>
<div class="partner" style="left:437px"><svg width="110" height="90" aria-hidden="true"><rect x="12" y="28" width="86" height="34" fill="none" stroke="#222" stroke-width="3"/></svg></div>
<div class="partner" style="left:612px"><svg width="110" height="90" aria-hidden="true"><rect x="14" y="30" width="82" height="30" fill="#222"/></svg></div>
<div class="partner" style="left:789px"><svg width="90" height="90" aria-hidden="true"><circle cx="45" cy="45" r="32" fill="none" stroke="#222" stroke-width="3"/></svg></div>
<div class="partner" style="left:963px"><svg width="90" height="90" aria-hidden="true"><rect x="18" y="18" width="54" height="54" fill="none" stroke="#222" stroke-width="3"/></svg></div>

<section class="section contact"></section>
<h2 class="section-title" style="top:2732px;color:var(--ink)">Contact Us</h2>
<div class="field" style="left:172px;top:2809px;width:414px;height:42px">Name</div>
<div class="field" style="left:612px;top:2809px;width:413px;height:42px">Phone Number</div>
<div class="field" style="left:172px;top:2867px;width:853px;height:184px">Message</div>
<a class="btn" style="left:524px;top:3071px;width:150px;height:40px;font-size:13px">Send Message</a>

<footer class="section site-footer"></footer>
<div class="footer-head" style="left:175px;top:3198px">Quick Links</div>
<ul class="footer-links"><li>Home</li><li>About</li><li>Upcoming Events</li><li>FAQS</li><li>contact us</li></ul>
<div class="footer-brand">Arena<br>on Draft</div>
<div class="socials"><span></span><span></span><span></span><span></span></div>
<div class="footer-head" style="left:878px;top:3198px">Our Address</div>
<div class="address">
  <b>Address</b>Lorem ipsum dolor sit amet street, suite four
  <b>Phone</b>1234567890
  <b>Email</b>hello@arenaondraft.com
</div>
<div class="copyright">Copyright © 2018 Arena on Draft. All Rights Reserved.</div>

</body>
</html>
```